Quorvix Letter head

Quorvix is a young and energetic software development consultancy. We spend our time working with clients to turn what ever is in their heads in to software.
We are trying to create an image of a high class software boutique who build class leading bespoke solutions.
We need a sharp letter head that looks great on high quality media.
We like bold colours and distinctive design. So show us what you can do.
Industry/Entity Type
Software
Requirements
Must have
- Our company is based in the UK and are requried to have on the paper somewhere the following information:
* Registered company name: Quorvix Ltd
* Registered company number
* VAT registration number
In addition we also want the following:
* An email address
* Telephone number
* Website address
An example of what some pages have in their footer is something like the following:
Quorvix Ltd is registered in England and Wales. Reg. no: 5316274
Registered office: 48 Cobblewick Road, Harlow Essex, CM93TP. Tel: 07712365081
You do not have to use this sentance but please make sure your design incorporates accommodates the requirements for UK based companies

```html
<!DOCTYPE html>
<html lang="en">
<head>
<meta charset="utf-8">
<title>Quorvix Letterhead</title>
<link rel="stylesheet" href="https://fonts.googleapis.com/css2?family=Source+Sans+3:wght@300;400;600&display=swap">
<style>
  :root {
    --backdrop: #858483;
    --paper: #ffffff;
    --brand-red: #a8222c;
    --brand-deep: #7c1820;
    --body-ink: #4a4a4a;
    --footer-ink: #b5b5b5;
  }
  * { margin: 0; padding: 0; box-sizing: border-box; }
  html, body { width: 849px; height: 1200px; overflow: hidden; }
  body {
    background: var(--backdrop);
    font-family: "Source Sans 3", Arial, sans-serif;
    position: relative;
  }
  .letterhead {
    position: absolute;
    left: 125px; top: 175px;
    width: 600px; height: 848px;
    background: var(--paper);
    overflow: hidden;
  }
  .band { position: absolute; left: 0; width: 600px; }
  .band--top { top: 0; height: 80px; }
  .band--bottom { bottom: 0; height: 90px; }
  .brand {
    position: absolute;
    left: 34px; top: 39px;
    font-size: 33px;
    font-weight: 400;
    letter-spacing: 1px;
    color: var(--brand-red);
    line-height: 1;
  }
  .letter-body {
    position: absolute;
    left: 35px; top: 206px;
    width: 458px;
    font-size: 11px;
    font-weight: 300;
    line-height: 14px;
    color: var(--body-ink);
  }
  .letter-body p { margin-bottom: 14px; text-align: justify; }
  .letter-body .salutation { font-weight: 600; margin-bottom: 0; color: #222; }
  .letter-body .product-list { list-style: none; margin-bottom: 14px; }
  .footer-info {
    position: absolute;
    right: 35px; top: 781px;
    text-align: right;
    font-size: 9.5px;
    font-weight: 300;
    line-height: 13px;
    color: var(--footer-ink);
  }
</style>
</head>
<body>
  <main class="letterhead">
    <svg class="band band--top" viewBox="0 0 600 80" aria-hidden="true">
      <polygon points="120,0 600,72 600,77 110,0" fill="var(--brand-deep)"/>
      <polygon points="195,0 600,0 600,65" fill="var(--brand-red)"/>
    </svg>

    <div class="brand">QUORVIX</div>

    <section class="letter-body">
      <p class="salutation">Dear Sirs,</p>
      <p>We are from PT. LUMEN ARTA SEJATI, Tbk. in this case intends to offering as cooperation with CV. TARUNA MEKAR to become a distributor of our products include:</p>
      <ul class="product-list">
        <li>electronic products</li>
        <li>Household furniture fixtures</li>
        <li>Furniture, etc..</li>
      </ul>
      <p>We will provide compensation comparable to the CV. Taruna MEKAR if willing to become an official distributor of the products of our company.</p>
      <p>Mechanisms of cooperation we can explain further if CV. Taruna MEKAR interested in the offer of cooperation that we submit.</p>
      <p>Thus this research agreement offer letter we make, for your attention and cooperation we say thank you.</p>
      <p>Nb: We will wait for a copy of Mr.. Rendi Kusuma CV as leader. Taruna MEKAR later than 14 days after this letter Mr.. receive.</p>
    </section>

    <svg class="band band--bottom" viewBox="0 0 600 90" aria-hidden="true">
      <polygon points="0,10 490,90 470,90 0,15" fill="var(--brand-deep)"/>
      <polygon points="0,28 0,90 455,90" fill="var(--brand-red)"/>
    </svg>

    <footer class="footer-info">
      <div>Quorvix Ltd is registered in England and Wales. Reg. no: 5316274</div>
      <div>Office: 48 Cobblewick Road, Harlow Essex, CM93TP.</div>
      <div>Tel: 07712365081</div>
    </footer>
  </main>
</body>
</html>
```